PowerPoint Template for Calmont

Cover Page, Table of Contents Page, and slide template that can be incorporated into table of contents, in an editable form. Using attached logo.

```html
<!DOCTYPE html>
<html lang="en">
<head>
<meta charset="utf-8">
<title>Calmont – Presentation Template</title>
<link href="https://fonts.googleapis.com/css2?family=Montserrat:wght@300;400;500;600;700&display=swap" rel="stylesheet">
<style>
:root{
  --bg:#000;
  --green:#7cc242;
  --green-mid:#5cb85c;
  --teal:#1fadb3;
  --teal-dark:#1a9ea4;
  --heading:#27a9ad;
  --body:#9a9a9a;
  --grey-box:#8c8c8c;
  --footer:#9b9b9b;
  --row-a:#e3f6f4;
  --row-b:#ececec;
  --white:#fff;
}
*{margin:0;padding:0;box-sizing:border-box}
html,body{width:1200px;height:911px;overflow:hidden;background:var(--bg);font-family:'Montserrat',sans-serif}
.board{position:relative;width:1200px;height:911px}
.slide{position:absolute;width:381px;height:285px;background:var(--white);overflow:hidden}
.c1{left:17px}.c2{left:413px}.c3{left:809px}
.r1{top:19px}.r2{top:315px}.r3{top:610px}
.header{position:absolute;left:0;top:0;width:100%;height:25px;background:linear-gradient(90deg,var(--green-mid),var(--teal));color:var(--white);font-weight:700;font-size:12.5px;line-height:25px;padding-left:6px}
.header .brand{position:absolute;right:6px;top:0;font-size:9px;font-weight:400;letter-spacing:1.5px}
.brand .dot{display:inline-block;width:4px;height:4px;border-radius:50%;background:currentColor;margin-right:3px;vertical-align:middle}
.footer{position:absolute;left:0;bottom:0;width:100%;height:10px;background:var(--footer);color:var(--white);font-size:4.5px;line-height:10px;padding-left:3px}
h3{color:var(--heading);font-weight:500;font-size:12px;position:absolute}
.txt{position:absolute;color:var(--body);font-size:5.6px;line-height:9px;text-align:justify}
.box{position:absolute;background:var(--grey-box)}
.centered{text-align:center}
/* cover */
.cover-top{position:absolute;left:0;top:0;width:100%;height:186px;background:linear-gradient(180deg,#8fc84a 0%,#5dbb6a 45%,#20adb2 100%)}
.cover-title{position:absolute;width:100%;text-align:center;color:var(--white);font-weight:300}
.logo-main{position:absolute;width:100%;text-align:center;color:var(--teal-dark);font-size:26px;font-weight:400;letter-spacing:3px}
.logo-main .dot{width:8px;height:8px;background:var(--green);margin-right:6px;vertical-align:middle;display:inline-block;border-radius:50%}
/* table */
.grid{position:absolute;left:25px;top:107px;width:341px;border-collapse:collapse;font-size:6.8px}
.grid th{background:var(--teal-dark);color:var(--white);font-weight:600;height:19px;text-align:left;padding-left:13px;font-size:6.2px}
.grid td{height:19px;padding-left:13px;color:#666}
.grid tr:nth-child(odd) td{background:var(--row-a)}
.grid tr:nth-child(even) td{background:var(--row-b)}
/* bio */
.avatar{position:absolute;width:82px;height:82px;border-radius:50%;background:linear-gradient(180deg,#e8e8e8,#bdbdbd)}
/* bullets */
.bullet{position:absolute;left:17px;color:var(--heading);font-size:10.5px;font-weight:500}
.bullet svg{vertical-align:-1px;margin-right:3px}
/* full gradient slides */
.full{background:linear-gradient(135deg,#7ec04a 0%,#4fb879 50%,#1faeb4 100%)}
.full .brand-lg{position:absolute;color:var(--white);font-size:18px;letter-spacing:2px}
.full .brand-lg .dot{display:inline-block;width:5px;height:5px;border-radius:50%;background:var(--white);margin-right:5px;vertical-align:middle}
</style>
</head>
<body>
<div class="board">

  <!-- Cover -->
  <section class="slide c1 r1">
    <div class="cover-top" role="img" aria-label="Laboratory photo with green to teal tint"></div>
    <div class="cover-title" style="top:99px;font-size:21px">Project Title here</div>
    <div class="cover-title" style="top:126px;font-size:14px">Subtext here</div>
    <div class="cover-title" style="top:158px;font-size:10px;font-weight:400">Persentator Name here</div>
    <div class="logo-main" style="top:234px"><span class="dot"></span>CALMONT</div>
    <div class="footer"></div>
  </section>

  <!-- Text + images -->
  <section class="slide c2 r1">
    <div class="header">Project Title Here<span class="brand"><span class="dot"></span>CALMONT</span></div>
    <h3 style="left:18px;top:60px">Images Text here</h3>
    <p class="txt" style="left:18px;top:79px;width:188px">Lorem Ipsum is simply dummy text of the printing and typesetting industry. Lorem Ipsum has been the industry's standard dummy text ever since the 1500s, when an unknown printer took a galley of type and scrambled it to make a type specimen book. It has survived not only five centuries</p>
    <p class="txt" style="left:18px;top:137px;width:188px">but also the leap into electronic typesetting, remaining essentially unchanged. It was popularised in the 1960s with the release of Letraset sheets containing Lorem Ipsum passages, and more recently with desktop publishing software like Aldus PageMaker including versions of Lorem Ipsum.</p>
    <p class="txt" style="left:18px;top:200px;width:188px">but also the leap into electronic typesetting, remaining essentially unchanged. It was popularised in the 1960s with the release of Letraset sheets containing Lorem Ipsum passages, and more recently with desktop publishing software like Aldus PageMaker including versions of Lorem Ipsum.</p>
    <div class="box" style="left:223px;top:59px;width:148px;height:92px"></div>
    <div class="box" style="left:223px;top:163px;width:148px;height:92px"></div>
    <div class="footer">Copyright text here</div>
  </section>

  <!-- Two images -->
  <section class="slide c3 r1">
    <div class="header">Project Title Here<span class="brand"><span class="dot"></span>CALMONT</span></div>
    <div class="box" style="left:17px;top:58px;width:148px;height:92px"></div>
    <div class="box" style="left:211px;top:58px;width:148px;height:92px"></div>
    <h3 style="left:17px;top:165px">Images Text here</h3>
    <h3 style="left:211px;top:165px">Images Text here</h3>
    <p class="txt" style="left:17px;top:184px;width:150px">Lorem Ipsum is simply dummy text of the printing and typesetting industry. Lorem Ipsum has been the industry's standard dummy text ever since the 1500s, when an unknown printer took a galley of type and scrambled it to make a type specimen book. It has survived not only five centuries</p>
    <p class="txt" style="left:211px;top:184px;width:150px">Lorem Ipsum is simply dummy text of the printing and typesetting industry. Lorem Ipsum has been the industry's standard dummy text ever since the 1500s, when an unknown printer took a galley of type and scrambled it to make a type specimen book. It has survived not only five centuries</p>
    <div class="footer">Copyright text here</div>
  </section>

  <!-- Table -->
  <section class="slide c1 r2">
    <div class="header">Project Title Here<span class="brand"><span class="dot"></span>CALMONT</span></div>
    <h3 style="left:25px;top:54px">Paragraph Text here</h3>
    <p class="txt" style="left:25px;top:73px;width:340px">Lorem Ipsum is simply dummy text of the printing and typesetting industry. Lorem Ipsum has been the industry's standard dummy text ever since the 1500s, when an unknown printer took a galley of type and scrambled it to make a type specimen book. It has survived not only five centuries</p>
    <table class="grid">
      <tr><th>Table Title Here</th><th>Table Title Here</th><th>Table Title Here</th><th>Table Title Here</th></tr>
      <tr><td>Table text here</td><td>Table text here</td><td>Table text here</td><td>Table text here</td></tr>
      <tr><td>Table text here</td><td>Table text here</td><td>Table text here</td><td>Table text here</td></tr>
      <tr><td>Table text here</td><td>Table text here</td><td>Table text here</td><td>Table text here</td></tr>
      <tr><td>Table text here</td><td>Table text here</td><td>Table text here</td><td>Table text here</td></tr>
      <tr><td>Table text here</td><td>Table text here</td><td>Table text here</td><td>Table text here</td></tr>
      <tr><td>Table text here</td><td>Table text here</td><td>Table text here</td><td>Table text here</td></tr>
    </table>
    <div class="footer">Copyright text here</div>
  </section>

  <!-- Bios -->
  <section class="slide c2 r2">
    <div class="header">Project Title Here<span class="brand"><span class="dot"></span>CALMONT</span></div>
    <div class="avatar" style="left:62px;top:64px" role="img" aria-label="Team member portrait"></div>
    <div class="avatar" style="left:240px;top:64px" role="img" aria-label="Team member portrait"></div>
    <h3 class="centered" style="left:20px;top:154px;width:168px">Bio Text here</h3>
    <h3 class="centered" style="left:198px;top:154px;width:168px">Bio Text here</h3>
    <p class="txt centered" style="left:37px;top:172px;width:135px;text-align:center">Lorem Ipsum is simply dummy text of the printing and typesetting industry. Lorem Ipsum has been the industry's standard dummy text ever since the 1500s, when an unknown printer took a galley of type and scrambled it to make a type specimen book. It has survived not only five centuries</p>
    <p class="txt centered" style="left:214px;top:172px;width:135px;text-align:center">Lorem Ipsum is simply dummy text of the printing and typesetting industry. Lorem Ipsum has been the industry's standard dummy text ever since the 1500s, when an unknown printer took a galley of type and scrambled it to make a type specimen book. It has survived not only five centuries</p>
    <div class="footer">Copyright text here</div>
  </section>

  <!-- Bullets -->
  <section class="slide c3 r2">
    <div class="header">Project Title Here<span class="brand"><span class="dot"></span>CALMONT</span></div>
    <div class="bullet" style="top:65px"><svg width="11" height="11"><circle cx="5.5" cy="5.5" r="4.5" fill="none" stroke="#27a9ad" stroke-width="1.4"/><circle cx="5.5" cy="5.5" r="2.5" fill="#7cc242"/></svg>Bullet text here</div>
    <p class="txt" style="left:30px;top:82px;width:336px;text-align:left">Lorem Ipsum is simply dummy text of the printing and typesetting industry. Lorem Ipsum has been the industry's standard dummy text ever since the 1500s, when an unknown printer took a galley of type and scrambled it to make a type specimen book. It has survived not only five centuries</p>
    <div class="bullet" style="top:123px"><svg width="11" height="11"><circle cx="5.5" cy="5.5" r="4.5" fill="none" stroke="#27a9ad" stroke-width="1.4"/><circle cx="5.5" cy="5.5" r="2.5" fill="#7cc242"/></svg>Bullet text here</div>
    <p class="txt" style="left:30px;top:140px;width:336px;text-align:left">Lorem Ipsum is simply dummy text of the printing and typesetting industry. Lorem Ipsum has been the industry's standard dummy text ever since the 1500s, when an unknown printer took a galley of type and scrambled it to make a type specimen book. It has survived not only five centuries</p>
    <div class="bullet" style="top:185px"><svg width="11" height="11"><circle cx="5.5" cy="5.5" r="4.5" fill="none" stroke="#27a9ad" stroke-width="1.4"/><circle cx="5.5" cy="5.5" r="2.5" fill="#7cc242"/></svg>Bullet text here</div>
    <p class="txt" style="left:30px;top:202px;width:336px;text-align:left">Lorem Ipsum is simply dummy text of the printing and typesetting industry. Lorem Ipsum has been the industry's standard dummy text ever since the 1500s, when an unknown printer took a galley of type and scrambled it to make a type specimen book. It has survived not only five centuries</p>
    <div class="footer">Copyright text here</div>
  </section>

  <!-- Two paragraphs -->
  <section class="slide c1 r3">
    <div class="header">Project Title Here<span class="brand"><span class="dot"></span>CALMONT</span></div>
    <h3 style="left:19px;top:65px;font-size:12.5px">Paragraph Text here</h3>
    <h3 style="left:203px;top:65px;font-size:12.5px">Paragraph Text here</h3>
    <p class="txt" style="left:19px;top:86px;width:158px">Lorem Ipsum is simply dummy text of the printing and typesetting industry. Lorem Ipsum has been the industry's standard dummy text ever since the 1500s, when an unknown printer took a galley of type and scrambled it to make a type specimen book. It has survived not only five centuries, but also the leap into electronic typesetting, remaining essentially unchanged. It was popularised in the 1960s with the release of Letraset sheets containing Lorem Ipsum passages, and more recently with desktop publishing software like Aldus PageMaker including versions of Lorem Ipsum.<br>It was popularised in the 1960s with the release of Letraset sheets containing Lorem Ipsum passages, and more recently with desktop publishing software like Aldus PageMaker including versions of Lorem Ipsum.</p>
    <p class="txt" style="left:203px;top:86px;width:158px">Lorem Ipsum is simply dummy text of the printing and typesetting industry. Lorem Ipsum has been the industry's standard dummy text ever since the 1500s, when an unknown printer took a galley of type and scrambled it to make a type specimen book. It has survived not only five centuries, but also the leap into electronic typesetting, remaining essentially unchanged. It was popularised in the 1960s with the release of Letraset sheets containing Lorem Ipsum passages, and more recently with desktop publishing software like Aldus PageMaker including versions of Lorem Ipsum.<br>It was popularised in the 1960s with the release of Letraset sheets containing Lorem Ipsum passages, and more recently with desktop publishing software like Aldus PageMaker including versions of Lorem Ipsum.</p>
    <div class="footer">Copyright text here</div>
  </section>

  <!-- Section divider -->
  <section class="slide c2 r3 full">
    <div class="brand-lg" style="left:18px;top:93px"><span class="dot"></span>CALMONT</div>
    <div style="position:absolute;left:18px;top:130px;color:#fff;font-weight:700;font-size:20px">Slide Section title here</div>
    <div style="position:absolute;left:18px;top:160px;color:#fff;font-size:12.5px">Sub section text here</div>
    <div class="footer">Copyright text here</div>
  </section>

  <!-- Thank you -->
  <section class="slide c3 r3 full">
    <div class="brand-lg" style="left:0;width:100%;text-align:center;top:104px;font-size:20px"><span class="dot"></span>CALMONT</div>
    <div style="position:absolute;left:0;width:100%;text-align:center;top:148px;color:#fff;font-weight:700;font-size:17.5px">THANKS FOR VALUBLE TIME</div>
    <div style="position:absolute;left:0;width:100%;text-align:center;top:183px;color:#fff;font-size:9.5px;line-height:15px">Contact details here<br>Contact details here 1<br>Contact details here 2</div>
    <div class="footer">Copyright text here</div>
  </section>

</div>
</body>
</html>
```